Brindle Logistics Business Card Design

We are a trucking and warehousing company. We run freight in the US manly from the Pacific NW to TX and back up the the PNW. We also do warehousing where we store, move, and distribute freight. Looking for a clean and modern design of business card. We would like to look rich and elegant. Attached is our logo.

Industry/Entity Type

Trucking Company

Contact Information for Business Card

Looking for a clean and modern design of business card. We would like to look rich and elegant.

Font styles to use
Sans Serif

Colors

Designer to choose colors to be used in the design.

Requirements
Must have
• logo but it should not dominate the card
Should not have
• logo should not dominate the card

```html
<!DOCTYPE html>
<html lang="en">
<head>
<meta charset="utf-8">
<title>Brindle Logistics Business Card</title>
<link href="https://fonts.googleapis.com/css2?family=Michroma&family=Open+Sans:wght@400;600&display=swap" rel="stylesheet">
<style>
  :root {
    --stage: #7a7a7a;
    --card-light: #eeeeee;
    --brand-blue: #0a6fbf;
    --brand-blue-deep: #0068b8;
    --accent-orange: #f2941c;
    --ink: #3a3a3a;
    --rule: #b5b5b5;
    --white: #ffffff;
  }
  html, body {
    margin: 0;
    padding: 0;
    width: 1200px;
    height: 1200px;
    overflow: hidden;
    background: var(--stage);
  }
  .canvas { position: relative; width: 1200px; height: 1200px; }
  .card {
    position: absolute;
    top: 310px;
    width: 364px;
    height: 594px;
    box-shadow: 2px 3px 4px rgba(0,0,0,0.35);
  }
  .card--front { left: 234px; background: var(--card-light); }
  .card--back  { left: 627px; width: 370px; background: var(--brand-blue-deep); }

  .wordmark {
    position: absolute;
    left: 0;
    right: 0;
    display: flex;
    align-items: center;
    justify-content: center;
    gap: 12px;
    font-family: "Open Sans", sans-serif;
    font-weight: 600;
    font-size: 23px;
    white-space: nowrap;
  }
  .wordmark__dot { width: 34px; height: 34px; border-radius: 50%; flex: none; }
  .card--front .wordmark { top: 156px; color: var(--brand-blue); }
  .card--front .wordmark__dot { background: var(--brand-blue); }
  .card--back .wordmark { top: 416px; color: var(--white); }
  .card--back .wordmark__dot { background: var(--white); }

  .contact {
    position: absolute;
    left: 0;
    right: 0;
    top: 336px;
    text-align: center;
    font-family: "Open Sans", sans-serif;
    color: var(--ink);
  }
  .contact__name {
    font-family: "Michroma", sans-serif;
    font-weight: 400;
    font-size: 19px;
    line-height: 24px;
    color: var(--brand-blue);
    margin: 0;
    letter-spacing: 0.5px;
  }
  .contact__name .surname { color: var(--accent-orange); }
  .contact__role { font-size: 16px; line-height: 22px; margin: 0; }
  .contact__rule { width: 208px; height: 1px; background: var(--rule); margin: 6px auto 9px; border: 0; }
  .contact__lines { font-size: 16px; line-height: 21.5px; margin: 0; }
  .label { color: var(--brand-blue); font-weight: 600; }
  .web { color: var(--brand-blue); font-weight: 600; }
  .web .domain { color: var(--accent-orange); }
  .contact__address { font-size: 16px; line-height: 21px; margin: 0; }

  .back-url {
    position: absolute;
    left: 0;
    right: 0;
    top: 536px;
    margin: 0;
    text-align: center;
    font-family: "Michroma", sans-serif;
    font-size: 14px;
    letter-spacing: 1px;
    color: var(--white);
  }
</style>
</head>
<body>
<main class="canvas">
  <section class="card card--front" aria-label="Business card front">
    <div class="wordmark">
      <span class="wordmark__dot"></span>
      <span class="wordmark__name">Brindle Logistics, LLC</span>
    </div>
    <div class="contact">
      <h1 class="contact__name">DANIEL <span class="surname">REYES</span></h1>
      <p class="contact__role">Managing Director</p>
      <hr class="contact__rule">
      <p class="contact__lines">
        <span class="label">P:</span> 503-555 014 277<br>
        <span class="label">M:</span> 503-555 014 277<br>
        <span class="label">E:</span> info@brindlehaul.com<br>
        <span class="web">www.<span class="domain">brindlehaul</span>.com</span>
      </p>
      <hr class="contact__rule">
      <p class="contact__address">4820 Cascade Depot Road<br>Portland, OR 97217.</p>
    </div>
  </section>

  <section class="card card--back" aria-label="Business card back">
    <div class="wordmark">
      <span class="wordmark__dot"></span>
      <span class="wordmark__name">Brindle Logistics, LLC</span>
    </div>
    <p class="back-url">WWW.BRINDLEHAUL.COM</p>
  </section>
</main>
</body>
</html>
```